Street Sign Project - Attract Customers

We need a street sign designed to display out the front of the building. It design will need to be 1800mm wide x 900mm high. We need to show potential customers where we are inviting. Some of the attachments are for inspiration. The sign will be printed on a sheet of aluminum. if you have a good look at our web site which is www.pk-r.com.au you should get a good feeling about the company and what we do.

Target Market(s)

Construction companies, landscaping and civil earth moving companies who may drive past our business

Industry/Entity Type

Building

Font styles to use
Sans Serif

Colors
ffffff
3277b5
000000

Requirements
Must have
• Company logo must be the main focus point
• The number "54" on the sign to show street number (300mm high)
• phone number - (02) 9418 3065
• web address - www.pk-r.com.au
• I have loaded pictures i would like to see used in the sign
Nice to have
• Banner picture as attached
Should not have
• Bright colours. Please use our blue colour where possible

```html
<!DOCTYPE html>
<html lang="en">
<head>
<meta charset="utf-8">
<title>Street Sign – Hauling &amp; Lifting Systems</title>
<link rel="stylesheet" href="https://fonts.googleapis.com/css2?family=Roboto+Condensed:wght@700&family=Roboto:wght@700&display=swap">
<style>
  :root {
    --sign-blue: #2a5fd6;
    --sign-green: #63d91c;
    --sign-light: #e4e9f1;
    --backdrop: #eceef1;
    --photo-a: #7f97ad;
    --photo-b: #4f86c6;
    --photo-c: #a5655a;
    --photo-d: #8d8c86;
    --photo-e: #6f9fd0;
  }
  * { margin: 0; padding: 0; box-sizing: border-box; }
  html, body { width: 1200px; height: 847px; overflow: hidden; background: var(--backdrop); }
  .canvas { position: relative; width: 1200px; height: 847px; }
  .sign {
    position: absolute; left: 40px; top: 143px; width: 1120px; height: 560px;
    background: var(--sign-blue); overflow: hidden;
    font-family: "Roboto Condensed", "Arial Narrow", sans-serif; font-weight: 700;
    color: var(--sign-light);
  }
  .sign-shapes { position: absolute; inset: 0; }
  .company-name {
    position: absolute; left: 86px; top: 60px; width: 600px;
    font-size: 80px; line-height: 80px; text-transform: uppercase; letter-spacing: 0.5px;
    font-weight: 700;
  }
  .company-name .line { display: block; height: 80px; margin-bottom: 22px; white-space: nowrap; }
  .company-name .suffix { font-size: 20px; letter-spacing: 2px; margin-left: 8px; }
  .street-number {
    position: absolute; left: 716px; top: 0; width: 404px; height: 272px;
  }
  .street-number .st {
    position: absolute; left: 18px; bottom: 30px; font-size: 58px; line-height: 1;
  }
  .street-number .num {
    position: absolute; left: 100px; top: 14px; font-size: 300px; line-height: 0.85;
    letter-spacing: -6px;
  }
  .contact {
    position: absolute; left: 722px; top: 284px; width: 380px;
    font-family: "Roboto", Arial, sans-serif; font-weight: 700; line-height: 1;
  }
  .contact .phone { display: block; font-size: 38px; letter-spacing: 1px; }
  .contact .web { display: block; font-size: 28px; margin-top: 8px; }
</style>
</head>
<body>
<div class="canvas">
  <div class="sign">
    <svg class="sign-shapes" width="1120" height="560" viewBox="0 0 1120 560">
      <rect class="number-block" x="716" y="0" width="404" height="272" fill="var(--sign-green)"/>
      <path class="lower-band" d="M0 425 Q560 410 1120 442 L1120 560 L0 560 Z" fill="var(--sign-green)"/>
      <g class="service-photos" stroke="var(--sign-green)" stroke-width="12">
        <ellipse cx="104" cy="452" rx="62" ry="82" fill="var(--photo-a)" role="img" aria-label="Photo of a materials hoist on scaffolding"/>
        <ellipse cx="277" cy="455" rx="70" ry="88" fill="var(--photo-b)" role="img" aria-label="Photo of a blue rubbish chute on a building"/>
        <ellipse cx="467" cy="458" rx="78" ry="92" fill="var(--photo-c)" role="img" aria-label="Photo of a ladder hoist on a tiled roof"/>
        <ellipse cx="680" cy="460" rx="86" ry="94" fill="var(--photo-d)" role="img" aria-label="Photo of a conveyor on a building site"/>
        <ellipse cx="925" cy="462" rx="100" ry="90" fill="var(--photo-e)" role="img" aria-label="Photo of a curved roller conveyor"/>
      </g>
    </svg>

    <h1 class="company-name">
      <span class="line">Hauling</span>
      <span class="line">&amp; Lifting</span>
      <span class="line">Systems<span class="suffix">Pty Ltd</span></span>
    </h1>

    <div class="street-number">
      <span class="st">St</span>
      <span class="num">54</span>
    </div>

    <div class="contact">
      <span class="phone">(02) 9418 3065</span>
      <span class="web">www.pk-r.com.au</span>
    </div>
  </div>
</div>
</body>
</html>
```